Webdesign für IT-Unternehmen / Spezialisierung auf Finanzdienstleistungen
Sehr professionell, sehr schnell und insgesamt ein sehr, sehr positiver Eindruck! Sehr empfehlenswert!!
Zielgruppe
Endlich eine digitale Beratungslösung für Sachwerte, die unabhängig allen Pools und Vermittlern zur Verfügung steht.
Anlageberater und -vermittler haben eine schwer überschaubare Vielzahl von Rechtsnormen und Vorschriften zu beachten, bevor ein Anleger seinen Zeichnungsschein unterschreiben kann. Bei Fehlern drohen Haftung und Schadensersatzforderungen. Nun kommt die neue Software kapmentor-7 an den Markt, die diese Situation zum Wohl der Berater verändern könnte. Dabei werden nicht nur die gesetzlichen Regelungen und Marktdirektiven wie MiFID-II berücksichtigt, sondern vielmehr auch auf die Usability, die Anwenderfreundlichkeit, geachtet. Dem Vermittler soll ein Werkzeug in die Hand gegeben werden, das ihn sowohl im Beratungsprozess selbst unterstützt, als auch mögliche Fehler bei der Formulareingabe vermeidet. Zusätzlich zu den bereits ausgefüllten Antragsformularen beim Abschluss wird ein auf den Kunden zugeschnittener Ex-Ante Kostenausweis erstellt, der gemeinsam mit allen notwendigen Unterlagen in einem komfortabel zusammengestellten PDF-Dokument per E-Mail versandt oder gedruckt werden kann.
Die Tessar Datenwerk GmbH mit Sitz in Lüneburg wurde 2020 gegründet und bietet eine unabhängige und vollelektronische Beratungslösung für Sachwerte an. Die Zielgruppe sind sowohl Pools, Vertriebe und Vermittler, allerdings auch Produktemittenten, welche ihre Produkte einem breiteren Markt anbieten wollen. Die in Österreich seit mehr als 20 Jahren tätige und renommierte Wendt & Kollegen Beratung GmbH, die mit ihren IT-Lösungen Banken, Pools und Vertriebe versorgt, steuert hierbei nicht nur die passende Software bei, sondern sorgt als Gesellschafter der Tessar Datenwerk GmbH auch für die Sicherheit und Weiterentwicklung der Software. Bernd Wendt, Eigentümer und Geschäftsführer der Wendt & Kollegen Beratung hat auch die Leitung der Tessar Datenwerk übernommen.
Aufgabenstellung
Onepager mit Wordpress, Farben in Anlehnung an unser Firmenlogo

```html
<!DOCTYPE html>
<html lang="de">
<head>
<meta charset="utf-8">
<title>kapmentor-7 – Vollelektronische Beratungslösung für Sachwerte</title>
<link href="https://fonts.googleapis.com/css2?family=Lato:wght@400;700&family=Poppins:wght@300;400;500;600&display=swap" rel="stylesheet">
<style>
:root{
  --brand:#0e4d7e;
  --brand-dark:#0b3e66;
  --accent:#f5b500;
  --ink:#111;
  --text:#3d3d3d;
  --frame:#444;
  --white:#fff;
  --line:#e3e3e3;
}
*{box-sizing:border-box;margin:0;padding:0}
html,body{width:1200px;height:2190px;overflow:hidden;background:var(--white)}
body{position:relative;font-family:'Poppins',sans-serif;color:var(--text)}
.topbar{position:absolute;left:0;top:0;width:1200px;height:37px;background:var(--brand);color:var(--white);font-family:'Lato',sans-serif;font-size:12px}
.topbar .contact-item{position:absolute;top:11px;display:flex;align-items:center;gap:8px}
.demo-cta{position:absolute;left:881px;top:0;width:192px;height:37px;background:var(--accent);color:var(--brand-dark);font-family:'Lato',sans-serif;font-weight:700;font-size:13px;display:flex;align-items:center;justify-content:center;gap:10px}
.mainnav{position:absolute;left:0;top:37px;width:1200px;height:72px;border-bottom:1px solid var(--line);background:var(--white);font-family:'Lato',sans-serif;font-size:11.5px;font-weight:700;color:#222}
.mainnav a{position:absolute;top:30px;color:inherit;text-decoration:none;letter-spacing:.2px;white-space:nowrap}
.mainnav a.active{color:var(--brand)}
.nav-indicator{position:absolute;left:226px;top:68px;width:111px;height:4px;background:var(--brand)}
.brand{position:absolute;left:510px;top:22px;display:flex;align-items:center;gap:6px;font-family:'Poppins',sans-serif;font-weight:500;font-size:24px;color:var(--brand)}
.brand-square{width:28px;height:28px;border:3px solid var(--brand)}
.band{position:absolute;left:0;width:1200px}
.hero{top:109px;height:475px;background:linear-gradient(100deg,#eef1f3 0%,#cdd6de 40%,#2d3d55 65%,#4a5d75 85%,#cfd6dc 100%);clip-path:polygon(0 0,100% 0,100% 475px,0 435px)}
.hero-frame{position:absolute;left:128px;top:181px;width:289px;height:297px;border:7px solid var(--frame)}
.hero-title{position:absolute;left:155px;top:236px;font-size:49px;line-height:59px;font-weight:300;color:var(--ink);letter-spacing:-.3px}
.hero-title strong{font-weight:600}
.about-band{top:540px;height:560px;background:linear-gradient(90deg,#b48a74 0%,#d9d3cc 30%,#eef0f1 60%,#e6e7e6 100%);clip-path:polygon(0 4px,100% 42px,100% 556px,0 515px)}
.code-band{top:1050px;height:560px;background:radial-gradient(ellipse at 62% 35%,#1c3a6a 0%,#0b1a3e 45%,#050c22 100%);clip-path:polygon(0 5px,100% 46px,100% 556px,0 516px)}
.contact-band{top:1565px;height:555px;background:linear-gradient(90deg,#173a58 0%,#2a5a7d 40%,#3f7396 70%,#3a6d90 100%);clip-path:polygon(0 1px,100% 41px,100% 553px,0 515px)}
.card{position:absolute;background:var(--white);width:473px;padding:28px 26px 0 35px;overflow:hidden}
.card h2{font-size:29px;font-weight:500;color:var(--brand);line-height:38px;letter-spacing:-.2px}
.card h2::after{content:"";display:block;width:30px;height:3px;background:var(--brand);margin-top:6px}
.card p{font-size:11.8px;font-weight:300;line-height:21px;color:#333;margin-top:15px;letter-spacing:-.05px}
.card p + p{margin-top:17px}
.about-card{left:600px;top:662px;height:345px}
.product-card{left:127px;top:1158px;height:345px}
.pill-btn{position:absolute;left:31px;top:278px;width:204px;height:40px;border-radius:20px;background:var(--brand);color:var(--white);font-family:'Lato',sans-serif;font-weight:700;font-size:13px;display:flex;align-items:center;justify-content:center;gap:10px}
.contact-card{left:600px;top:1686px;height:345px}
.field{position:absolute;border:2px solid var(--brand);border-radius:3px;font-size:12px;color:#555;padding:11px 14px}
.send-btn{position:absolute;left:107px;top:289px;width:258px;height:41px;background:var(--brand);color:var(--white);font-size:15px;font-weight:500;letter-spacing:.5px;display:flex;align-items:center;justify-content:center;gap:12px}
.footer{position:absolute;left:0;top:2110px;width:1200px;height:80px}
.footer-brand{position:absolute;left:128px;top:21px;display:flex;align-items:center;gap:6px;font-weight:500;font-size:15px;color:var(--brand)}
.footer-brand .brand-square{width:20px;height:20px;border-width:2px}
.footer-nav{position:absolute;left:385px;top:32px;display:flex;gap:25px;font-family:'Lato',sans-serif;font-size:12px;font-weight:700;color:#333}
.social{position:absolute;left:960px;top:30px;display:flex;gap:14px;font-size:11px;font-weight:500;color:var(--brand)}
</style>
</head>
<body>

<header class="topbar">
  <div class="contact-item" style="left:127px">
    <svg width="16" height="11" viewBox="0 0 16 11" fill="none" stroke="#fff" stroke-width="1.2"><rect x=".6" y=".6" width="14.8" height="9.8"/><path d="M.6 .6 8 6.5 15.4 .6"/></svg>
    kontakt@kapmentor-7.de
  </div>
  <div class="contact-item" style="left:323px">
    <svg width="13" height="13" viewBox="0 0 13 13" fill="none" stroke="#fff" stroke-width="1.2"><path d="M3 1 5 4 3.7 5.4C4.5 7.2 5.8 8.5 7.6 9.3L9 8l3 2-1.3 2C6 12 1 7 1 2.3Z"/></svg>
    1800.555.0142
  </div>
  <div class="demo-cta">
    <svg width="18" height="14" viewBox="0 0 18 14" fill="none" stroke="#0b3e66" stroke-width="1.3"><circle cx="3.5" cy="3" r="1.8"/><path d="M1 13V7h5l4-2M3.5 7v6"/><rect x="8" y="1" width="9" height="8"/><path d="M10 3.5h5M10 6h5"/></svg>
    Bestellung einer Demo
  </div>
</header>

<nav class="mainnav">
  <a class="active" style="left:237px">UNTERNEHMEN</a>
  <a style="left:352px">ÜBER UNS</a>
  <div class="brand"><span class="brand-square"></span>kapmentor-7</div>
  <a style="left:790px">PRODUKT KAPMENTOR-7</a>
  <a style="left:955px">KONTAKT</a>
  <span class="nav-indicator"></span>
</nav>

<section class="band hero" role="img" aria-label="Zwei Berater im Anzug besprechen Unterlagen in einem hellen Büro"></section>
<div class="hero-frame"></div>
<h1 class="hero-title">Vollelektronische<br>Beratungslösung<br>für <strong>Sachwerte</strong></h1>

<section class="band about-band" role="img" aria-label="Team arbeitet an Schreibtischen in einem offenen Büro mit Backsteinwand"></section>
<article class="card about-card">
  <h2>Über Uns</h2>
  <p>Duis aute irure dolor in reprehenderit in voluptate velit esse cillum dolore eu fugiat nulla pariatur. Excepteur sint occaecat cupidatat non proident, sunt in culpa qui officia deserunt mollit anim id est laborum. Lorem ipsum dolor sit amet, consectetur adipiscing elit, sed do eiusmod tempor incididunt ut labore et dolore magna aliqua.</p>
  <p>Ut enim ad minim veniam, quis nostrud exercitation ullamco laboris nisi ut aliquip ex ea commodo consequat. Duis aute irure dolor in reprehenderit in voluptate velit esse cillum dolore eu fugiat nulla pariatur. Excepteur sint occaecat cupidatat non proident, sunt in culpa qui officia deserunt mollit anim id est laborum.</p>
</article>

<section class="band code-band" role="img" aria-label="Programmcode in gelber Schrift auf dunkelblauem Bildschirm"></section>
<article class="card product-card">
  <h2>Produkt kapmentor-7</h2>
  <p>Duis aute irure dolor in reprehenderit in voluptate velit esse cillum dolore eu fugiat nulla pariatur. Excepteur sint occaecat cupidatat non proident, sunt in culpa qui officia deserunt mollit anim id est laborum. Lorem ipsum dolor sit amet, consectetur adipiscing elit, sed do eiusmod tempor incididunt ut labore et dolore magna aliqua.</p>
  <p>Ut enim ad minim veniam, quis nostrud exercitation ullamco laboris nisi ut aliquip ex ea commodo consequat.</p>
  <div class="pill-btn">
    <svg width="18" height="14" viewBox="0 0 18 14" fill="none" stroke="#fff" stroke-width="1.3"><circle cx="3.5" cy="3" r="1.8"/><path d="M1 13V7h5l4-2M3.5 7v6"/><rect x="8" y="1" width="9" height="8"/><path d="M10 3.5h5M10 6h5"/></svg>
    Bestellung einer Demo
  </div>
</article>

<section class="band contact-band" role="img" aria-label="Hand hält ein Smartphone mit leuchtenden Kommunikationssymbolen vor blauem Hintergrund"></section>
<article class="card contact-card">
  <h2>Kontact</h2>
  <div class="field" style="left:36px;top:78px;width:195px;height:42px">First Name</div>
  <div class="field" style="left:242px;top:78px;width:196px;height:42px">Last Name</div>
  <div class="field" style="left:36px;top:131px;width:195px;height:43px">Email</div>
  <div class="field" style="left:242px;top:131px;width:196px;height:43px">Phone</div>
  <div class="field" style="left:36px;top:182px;width:402px;height:95px">Comments</div>
  <div class="send-btn">
    <svg width="16" height="16" viewBox="0 0 16 16" fill="none" stroke="#fff" stroke-width="1.3"><path d="M15 1 1 7l5 2 2 6Z M6 9l9-8"/></svg>
    SENDEN
  </div>
</article>

<footer class="footer">
  <div class="footer-brand"><span class="brand-square"></span>kapmentor-7</div>
  <div class="footer-nav"><span>UNTERNEHMEN</span><span>ÜBER UNS</span><span>PRODUKT KAPMENTOR-7</span><span>KONTAKT</span></div>
  <div class="social"><span>Sozial</span><span>Foto</span><span>Video</span></div>
</footer>

</body>
</html>
```